Corrigan Construction Law P.A.

Business Card with Corporate Logo. For a law firm specializing in construction law.

need address, telephone, email and website. Also, have an elegant and conservative logo.

Logo so it is RBN.

Full name "Gordon T. Corrigan

Under my name title "Attorney at Law"

Under title "Board Certified in Construction Law"

PA in email is lower case

Add logo to back side of card

Mix in a bit of gold color into card to go with the green

Some color on bottom
Updates

Target Market(s)

legal

Industry/Entity Type

Construction

Contact Information for Business Card

I like it -- edits: 1. add "L" to logo so it is RBN. 2. add my full name "Gordon T. Business Card with Corporate Logo. For a law firm specializing in construction law.

Logo so it is RBN.

PA in email is lower case

Font styles to use
Serif

Colors
00a990
f78f20

Requirements
Must have
• Conservative legal designed logo for construction market
• Address:
• Corrigan Construction Law, P.A.
• 4150 Meadowlark Ave North, Ste B4
• Jacksonville, Florida 32217
• Main: 904-555-3172
• Direct: 904-555-8410
• Fax: 904-555-8410
• gt@corriganpa-example.com
• www.corriganbuildlaw-example.com
Nice to have
• Catchy conservative logo on card
Should not have
• Flashy

```html
<!DOCTYPE html>
<html lang="en">
<head>
<meta charset="utf-8">
<title>Corrigan Construction Law, P.A. – Business Card</title>
<link rel="stylesheet" href="https://fonts.googleapis.com/css2?family=Arimo:wght@400;700&family=Source+Sans+3:wght@400;600&display=swap">
<style>
  :root {
    --backdrop: #e9e6e1;
    --card: #ffffff;
    --gold: #e2a832;
    --teal: #2aa88e;
    --ink: #111111;
    --text: #1e1e1e;
    --brand-ink: #231f1c;
  }
  html, body {
    margin: 0;
    padding: 0;
    width: 1200px;
    height: 1000px;
    overflow: hidden;
    background: var(--backdrop);
  }
  .canvas {
    position: relative;
    width: 1200px;
    height: 1000px;
  }
  .card {
    position: absolute;
    left: 263px;
    width: 673px;
    height: 406px;
    background: var(--card);
    box-shadow: 0 3px 10px rgba(0,0,0,0.18);
    overflow: hidden;
  }
  .card--front { top: 59px; }
  .card--back {
    top: 528px;
    display: flex;
    align-items: center;
    justify-content: center;
  }

  .band { position: absolute; left: 0; width: 100%; height: 17px; }
  .band--top { top: 0; background: var(--gold); }
  .band--bottom { bottom: 0; background: var(--teal); }

  .identity {
    position: absolute;
    top: 65px;
    left: 0;
    width: 100%;
    text-align: center;
  }
  .identity__name {
    margin: 0;
    font-family: "Arimo", Arial, sans-serif;
    font-weight: 700;
    font-size: 24px;
    letter-spacing: 0.5px;
    color: var(--ink);
    line-height: 30px;
  }
  .identity__title {
    margin: 0;
    font-family: "Source Sans 3", "Myriad Pro", sans-serif;
    font-weight: 400;
    font-size: 28px;
    line-height: 32px;
    color: var(--gold);
  }
  .identity__title--first { margin-top: 4px; }

  .contact {
    position: absolute;
    font-family: "Arimo", Arial, sans-serif;
    font-size: 20px;
    line-height: 23px;
    color: var(--text);
  }
  .contact p { margin: 0; white-space: nowrap; }
  .contact__icon {
    position: absolute;
    left: -30px;
    top: 2px;
    width: 20px;
    height: 20px;
    fill: var(--ink);
  }
  .contact--address { left: 83px; top: 188px; }
  .contact--phone { left: 469px; top: 194px; }
  .contact--email { left: 224px; top: 297px; }
  .contact--web { left: 224px; top: 329px; }
  .contact--address .contact__icon { top: 0; }

  .brand {
    display: flex;
    align-items: center;
    gap: 18px;
  }
  .brand__square {
    width: 72px;
    height: 72px;
    background: var(--gold);
  }
  .brand__name {
    margin: 0;
    font-family: "Arimo", Arial, sans-serif;
    font-weight: 700;
    font-size: 22px;
    line-height: 26px;
    letter-spacing: 0.3px;
    color: var(--brand-ink);
    text-transform: uppercase;
  }
</style>
</head>
<body>
<main class="canvas">

  <section class="card card--front" aria-label="Business card front">
    <div class="band band--top"></div>

    <header class="identity">
      <h1 class="identity__name">Gordon T. Corrigan</h1>
      <p class="identity__title identity__title--first">Attorney at Law</p>
      <p class="identity__title">Board Certified in Construction Law</p>
    </header>

    <div class="contact contact--address">
      <svg class="contact__icon" viewBox="0 0 20 20" aria-hidden="true">
        <path d="M10 1 L1 8 H19 Z"/>
        <rect x="2" y="9" width="16" height="10"/>
        <rect x="5" y="12" width="5" height="3" fill="#fff"/>
      </svg>
      <p>Corrigan Construction Law, P.A.</p>
      <p>4150 Meadowlark Ave N Ste B4</p>
      <p>Jacksonville, FL 32217</p>
    </div>

    <div class="contact contact--phone">
      <svg class="contact__icon" viewBox="0 0 20 20" aria-hidden="true">
        <path d="M6 2 C3 3 2 7 4 11 C6 15 9 18 13 19 L15 15 L12 13 L10 14 C8 12 7 10 7 8 L9 6 L8 2 Z"/>
      </svg>
      <p>904-555-3172</p>
      <p>904-555-8410</p>
    </div>

    <div class="contact contact--email">
      <svg class="contact__icon" viewBox="0 0 20 20" aria-hidden="true">
        <rect x="2" y="5" width="16" height="11"/>
        <path d="M2 5 L10 11 L18 5" fill="none" stroke="#fff" stroke-width="1.6"/>
      </svg>
      <p>gt@corriganpa-example.com</p>
    </div>

    <div class="contact contact--web">
      <svg class="contact__icon" viewBox="0 0 20 20" aria-hidden="true">
        <g fill="none" stroke="#111" stroke-width="1.6">
          <circle cx="10" cy="10" r="8"/>
          <ellipse cx="10" cy="10" rx="3.5" ry="8"/>
          <line x1="2" y1="10" x2="18" y2="10"/>
          <line x1="3.5" y1="6" x2="16.5" y2="6"/>
          <line x1="3.5" y1="14" x2="16.5" y2="14"/>
        </g>
      </svg>
      <p>www.corriganbuildlaw-example.com</p>
    </div>

    <div class="band band--bottom"></div>
  </section>

  <section class="card card--back" aria-label="Business card back">
    <div class="brand">
      <div class="brand__square"></div>
      <p class="brand__name">Corrigan<br>Construction<br>Law</p>
    </div>
  </section>

</main>
</body>
</html>
```